Laundromat Grand Opening.

Laundromat /Grand opening. One side English, one side Spanish. Include the Address, Name, Raffle/Prizes and Grand opening date.
Elmridge Wash Laundromat, 415 W. Harlan Ave. 2/7/2016. (555) 314-2297.

Coin

000000

• Eye catching. Laundry theme.

```html
<!DOCTYPE html>
<html lang="en">
<head>
<meta charset="utf-8">
<title>Elmridge Wash Laundromat – Grand Opening</title>
<link rel="stylesheet" href="https://fonts.googleapis.com/css2?family=Oswald:wght@600&family=Tinos:wght@700&family=Roboto+Condensed:wght@400;700&family=Lato:wght@400&display=swap">
<style>
  :root {
    --red: #e0303c;
    --red-deep: #8e0c14;
    --ink: #1c1c1c;
    --black: #141414;
    --white: #ffffff;
    --photo-a: #9aa3ad;
    --photo-b: #3b4252;
  }
  html, body { margin: 0; padding: 0; overflow: hidden; background: var(--white); }
  .flyer {
    position: relative;
    width: 1200px;
    height: 907px;
    overflow: hidden;
    background: var(--white);
    font-family: "Lato", sans-serif;
  }
  .flyer-art { position: absolute; inset: 0; }
  .business-name {
    position: absolute;
    left: 24px; top: 40px;
    margin: 0;
    font-family: "Oswald", sans-serif;
    font-weight: 600;
    font-size: 50px;
    letter-spacing: 0.5px;
    color: var(--ink);
    white-space: nowrap;
  }
  .business-name .accent { color: var(--red); }
  .headline {
    position: absolute;
    left: 30px; top: 168px;
    margin: 0;
    font-family: "Tinos", serif;
    font-weight: 700;
    font-size: 124px;
    line-height: 118px;
    color: #f2f2f2;
    text-shadow: 0 3px 4px rgba(0,0,0,0.35);
  }
  .date-sign {
    position: absolute;
    left: 92px; top: 498px;
    width: 299px; height: 196px;
    display: flex; flex-direction: column; align-items: center; justify-content: center;
    font-family: "Roboto Condensed", sans-serif;
    color: var(--ink);
  }
  .date-sign .on { font-size: 50px; line-height: 56px; }
  .date-sign .date { font-size: 62px; line-height: 70px; }
  .prize-badge {
    position: absolute;
    left: 545px; top: 566px;
    width: 300px; height: 220px;
    display: flex; flex-direction: column; align-items: center; justify-content: center;
    font-family: "Roboto Condensed", sans-serif;
    font-weight: 700;
    font-size: 56px;
    line-height: 66px;
    color: #eeeeee;
    text-shadow: 0 2px 3px rgba(0,0,0,0.4);
  }
  .contact {
    position: absolute;
    left: 72px; top: 774px;
    margin: 0; padding: 0;
    list-style: none;
    color: var(--white);
    font-size: 26px;
    line-height: 32px;
  }
  .contact li { display: flex; align-items: flex-start; gap: 22px; margin-bottom: 12px; }
  .contact svg { flex: none; margin-top: 4px; }
</style>
</head>
<body>
<div class="flyer">
  <svg class="flyer-art" width="1200" height="907" viewBox="0 0 1200 907" aria-hidden="true">
    <defs>
      <linearGradient id="bandRed" x1="0" y1="0" x2="0" y2="1">
        <stop offset="0" stop-color="#f03a45"/>
        <stop offset="1" stop-color="#8e0c14"/>
      </linearGradient>
      <linearGradient id="signFill" x1="0" y1="0" x2="0" y2="1">
        <stop offset="0" stop-color="#ffffff"/>
        <stop offset="1" stop-color="#cfcfcf"/>
      </linearGradient>
      <radialGradient id="badgeFill" cx="0.5" cy="0.35" r="0.7">
        <stop offset="0" stop-color="#e0303c"/>
        <stop offset="1" stop-color="#7a0a10"/>
      </radialGradient>
      <linearGradient id="darkFill" x1="0" y1="0" x2="0" y2="1">
        <stop offset="0" stop-color="#2a2a2a"/>
        <stop offset="1" stop-color="#0d0d0d"/>
      </linearGradient>
    </defs>

    <!-- headline band -->
    <rect x="0" y="136" width="760" height="6" fill="var(--black)"/>
    <rect x="0" y="148" width="780" height="314" fill="url(#bandRed)"/>
    <rect x="0" y="462" width="780" height="6" fill="var(--black)"/>

    <!-- porthole frame -->
    <circle cx="953" cy="368" r="305" fill="var(--black)"/>
    <circle cx="953" cy="368" r="286" fill="var(--white)"/>
    <circle cx="953" cy="368" r="276" fill="#2b2b2b"/>
    <circle cx="953" cy="368" r="262" fill="var(--white)"/>
    <circle cx="953" cy="368" r="256" fill="var(--black)"/>

    <!-- bottom swoosh -->
    <path d="M0 700 C 300 714, 520 758, 760 746 S 1100 632, 1200 600 L1200 907 L0 907 Z" fill="var(--red)"/>
    <path d="M0 716 C 300 732, 520 780, 780 770 S 1100 664, 1200 640 L1200 907 L0 907 Z" fill="var(--white)"/>
    <path d="M0 732 C 300 748, 520 798, 790 788 S 1100 690, 1200 668 L1200 907 L0 907 Z" fill="url(#darkFill)"/>

    <!-- hanging sign -->
    <line x1="250" y1="445" x2="150" y2="510" stroke="var(--ink)" stroke-width="3"/>
    <line x1="250" y1="445" x2="340" y2="510" stroke="var(--ink)" stroke-width="3"/>
    <rect x="92" y="498" width="299" height="196" rx="22" fill="url(#signFill)" stroke="#bdbdbd" stroke-width="2"/>
    <circle cx="250" cy="442" r="9" fill="var(--red)"/>

    <!-- prize starburst -->
    <polygon fill="var(--white)" stroke="var(--red)" stroke-width="4" points="
      695,520 715,548 745,530 757,562 792,555 792,590 826,596 812,627 842,645 815,667 842,690 810,705 826,738 792,742 792,778 757,770 745,802 715,783 695,812 675,783 645,802 633,770 598,778 598,742 564,738 580,705 548,690 575,667 548,645 578,627 564,596 598,590 598,555 633,562 645,530 675,548"/>
    <circle cx="695" cy="666" r="118" fill="url(#badgeFill)"/>
  </svg>

  <svg class="flyer-art" width="1200" height="907" viewBox="0 0 1200 907" role="img" aria-label="Photo: woman loading laundry into a washing machine, seen from inside the drum">
    <defs>
      <linearGradient id="photoFill" x1="0" y1="0" x2="0" y2="1">
        <stop offset="0" stop-color="var(--photo-a)"/>
        <stop offset="1" stop-color="var(--photo-b)"/>
      </linearGradient>
    </defs>
    <circle cx="953" cy="368" r="246" fill="url(#photoFill)"/>
  </svg>

  <h1 class="business-name">ELMRIDGE WASH <span class="accent">LAUNDROMAT</span></h1>
  <h2 class="headline">GRAND<br>OPENING</h2>

  <div class="date-sign">
    <span class="on">ON</span>
    <span class="date">2-7-2016</span>
  </div>

  <div class="prize-badge">
    <span>OFFER</span>
    <span>PRIZES</span>
  </div>

  <ul class="contact">
    <li>
      <svg width="24" height="24" viewBox="0 0 24 24" aria-hidden="true"><path d="M6.6 10.8c1.4 2.8 3.8 5.1 6.6 6.6l2.2-2.2c.3-.3.7-.4 1-.2 1.1.4 2.3.6 3.6.6.6 0 1 .4 1 1V20c0 .6-.4 1-1 1C10.6 21 3 13.4 3 4c0-.6.4-1 1-1h3.5c.6 0 1 .4 1 1 0 1.3.2 2.5.6 3.6.1.3 0 .7-.2 1z" fill="var(--red)"/></svg>
      <span>(555) 314-2297</span>
    </li>
    <li>
      <svg width="24" height="30" viewBox="0 0 24 30" aria-hidden="true"><path d="M12 0C5.9 0 1 4.9 1 11c0 8 11 19 11 19s11-11 11-19C23 4.9 18.1 0 12 0zm0 15a4 4 0 110-8 4 4 0 010 8z" fill="var(--red)"/></svg>
      <span>415 W. Harlan Ave.<br>Elmridge, CA 91750</span>
    </li>
  </ul>
</div>
</body>
</html>
```